Eye surgeon needs a presentation folder and a business card for his practice manager. Logo alread...

I need a folder to put papers in when I am scheduling patients for surgery. The information is general, such as costs, consent forms etc. The folder is designed to give the patient these papers in a neat manner. The cover of the folder needs to use my brand and perhaps create some interest when it is sitting on their kitchen bench with visitors and family. I'll attach a typical template for a folder. It needs to be stylish, classic and professional, as I am about to operate on the person's eye. <br/>I would like my logo included. I'll also attach a photo which is on my website which might work to wrap around the folder. The website address is raybelford.com.au and you can see the way the image is used there on most of the pages as a banner. My profile photo could possibly used as well. Perhaps on the back, but if it looks strange then that is not necessary. The contact information need not be on the folder. Just Dr Ray Belford, Ophthalmic Surgeon. Finally, our brand slogan is. "The world's a beautiful place, see it clearly". This could also be on it. Again, this all needs to be professional looking. <br/>I've attached all our previous design jobs, 2 profile pictures, and the image that I think would work. Please also look at the website. <br/><br/>The second part of the project is to create a business card for my practice manager. Her name is Miriam Holtby<br/>It should include<br/>Miriam Holtby (BCom)<br/>Practice Manager for Dr Ray Belford<br/>Ophthalmic Surgeon <br/><br/>Then all the details which are on our current business card<br/><br/><br/><br/><br/>

Contact Information for Business Card

Just match the business cards I already have, but use the details above

Colors

Designer to choose colors to be used in the design.

```html
<!DOCTYPE html>
<html lang="en">
<head>
<meta charset="utf-8">
<title>Dr Ray Belford – Presentation Folder</title>
<link href="https://fonts.googleapis.com/css2?family=Lato:wght@400;700&display=swap" rel="stylesheet">
<style>
  :root {
    --page-bg: #d9dadc;
    --brand-blue: #1b78bf;
    --brand-blue-deep: #135f9e;
    --brand-blue-light: #2fa3dc;
    --header-white: #f3f3f1;
    --text-white: #ffffff;
    --text-dark: #3b3b3b;
    --photo-grey: #6a6a68;
    --photo-amber: #b98a4a;
    --photo-dark: #2a2621;
    --portrait-tone: #b7ab98;
    --portrait-tone-light: #c9bfae;
  }
  * { box-sizing: border-box; margin: 0; padding: 0; }
  html, body { width: 1200px; height: 847px; overflow: hidden; }
  body {
    background: var(--page-bg);
    font-family: "Lato", Arial, sans-serif;
    display: flex; align-items: center; justify-content: center;
  }
  .folder-spread { display: flex; width: 1140px; height: 800px; box-shadow: 0 6px 24px rgba(0,0,0,.25); }
  .panel { position: relative; width: 570px; height: 800px; overflow: hidden; }

  /* Back cover */
  .back-cover {
    background: radial-gradient(circle at 60% 55%, var(--brand-blue-light) 0%, var(--brand-blue) 45%, var(--brand-blue-deep) 100%);
  }
  .pattern-layer {
    position: absolute; inset: 0;
    background: linear-gradient(135deg, rgba(255,255,255,.06) 0%, rgba(255,255,255,.02) 50%, rgba(255,255,255,.06) 100%);
  }
  .portrait {
    position: absolute; left: 50px; bottom: 0; width: 360px; height: 330px;
    background: linear-gradient(180deg, var(--portrait-tone-light) 0%, var(--portrait-tone) 100%);
    opacity: .9;
  }

  /* Front cover */
  .front-cover { background: var(--header-white); }
  .masthead { height: 150px; display: flex; align-items: center; justify-content: center; gap: 16px; }
  .brand-mark { width: 60px; height: 60px; border-radius: 50%; background: var(--brand-blue); }
  .brand-text { display: flex; flex-direction: column; }
  .brand-name { font-weight: 700; font-size: 32px; color: var(--brand-blue); line-height: 1.05; }
  .brand-role { font-weight: 700; font-size: 13px; color: var(--text-dark); margin-left: 8px; }
  .brand-credentials { font-size: 10px; color: var(--text-dark); margin-left: 10px; }
  .accent-rule { height: 10px; background: linear-gradient(90deg, var(--brand-blue-deep), var(--brand-blue-light), var(--brand-blue-deep)); }
  .hero {
    position: relative; height: 490px;
    background: linear-gradient(180deg, var(--photo-grey) 0%, var(--photo-amber) 45%, var(--photo-dark) 100%);
  }
  .slogan {
    position: absolute; top: 30px; width: 100%; text-align: center;
    color: var(--text-white); font-weight: 700; font-size: 28px; line-height: 1.3;
    text-shadow: 0 1px 3px rgba(0,0,0,.35);
  }
  .title-band {
    height: 150px; display: flex; flex-direction: column; justify-content: center; align-items: center;
    background: linear-gradient(90deg, var(--brand-blue) 0%, var(--brand-blue-light) 55%, var(--brand-blue-deep) 100%);
    color: var(--text-white);
  }
  .title-name { font-size: 44px; font-weight: 400; line-height: 1.15; }
  .title-role { font-size: 40px; font-weight: 400; line-height: 1.15; }
</style>
</head>
<body>
  <main class="folder-spread">
    <section class="panel back-cover">
      <div class="pattern-layer" role="img" aria-label="Faint repeating pattern of the practice mark over the blue background"></div>
      <div class="portrait" role="img" aria-label="Portrait photo of Dr Ray Belford in a beige blazer and white shirt"></div>
    </section>

    <section class="panel front-cover">
      <header class="masthead">
        <span class="brand-mark"></span>
        <div class="brand-text">
          <span class="brand-name">Dr Ray Belford</span>
          <span class="brand-role">Ophthalmic Surgeon</span>
          <span class="brand-credentials">MBBS (Hons) MMed FRANZCO</span>
        </div>
      </header>
      <div class="accent-rule"></div>
      <div class="hero" role="img" aria-label="Photo of a sunset over the ocean seen from a boat, with a fishing rod in the corner">
        <p class="slogan">The world's a beautiful place,<br>see it clearly</p>
      </div>
      <footer class="title-band">
        <span class="title-name">Dr Ray Belford,</span>
        <span class="title-role">Ophthalmic Surgeon.</span>
      </footer>
    </section>
  </main>
</body>
</html>
```